Automotive Business Card Design

I would just like a automotive themed card. nothing too extravagant, but catchy.

needs to say something about doing roadside assistance,mobile repairs, Diesel repairs, and Fleet maintenance

it can be single sided or double sided. no preference there.

Industry/Entity Type

Automotive

Contact Information for Business Card

Dean Marwick
phone 519 374 2083
Name: Brightway Automotive & Diesel Repair

```html
<!DOCTYPE html>
<html lang="en">
<head>
<meta charset="utf-8">
<title>Brightway Automotive &amp; Diesel Repair — Business Card</title>
<link href="https://fonts.googleapis.com/css2?family=Lato:wght@400&family=Montserrat:wght@700&display=swap" rel="stylesheet">
<style>
  :root {
    --backdrop: #202020;
    --card-light: #ffffff;
    --card-dark: #262626;
    --ink: #222222;
    --gold: #9e7e4e;
    --shadow: rgba(0, 0, 0, 0.45);
  }
  * { margin: 0; padding: 0; box-sizing: border-box; }
  html, body {
    width: 1029px;
    height: 1200px;
    overflow: hidden;
    background: var(--backdrop);
  }
  .canvas {
    position: relative;
    width: 1029px;
    height: 1200px;
  }
  .card {
    position: absolute;
    left: 66px;
    width: 899px;
    height: 513px;
    box-shadow: 0 4px 10px var(--shadow);
    color: var(--ink);
  }
  .card--front { top: 63px; background: var(--card-light); }
  .card--back  { top: 624px; background: var(--card-dark); color: var(--gold); }

  .contact-line {
    position: absolute;
    top: 34px;
    left: 0;
    width: 100%;
    text-align: center;
    font-family: "Lato", sans-serif;
    font-weight: 400;
    font-size: 35px;
    line-height: 40px;
  }
  .wordmark {
    position: absolute;
    top: 150px;
    left: 0;
    width: 100%;
    text-align: center;
    font-family: "Montserrat", sans-serif;
    font-weight: 700;
  }
  .wordmark__name {
    display: block;
    font-size: 76px;
    line-height: 86px;
    letter-spacing: 2px;
  }
  .wordmark__trade {
    display: block;
    margin-top: 12px;
    font-size: 22px;
    line-height: 28px;
    letter-spacing: 2.5px;
  }
  .divider {
    position: absolute;
    left: 0;
    top: 410px;
    width: 100%;
    height: 5px;
    background: var(--ink);
  }
  .card--front .divider { background: var(--backdrop); }
  .card--back .divider { height: 4px; background: var(--gold); }

  .services {
    position: absolute;
    top: 454px;
    left: 0;
    width: 100%;
    text-align: center;
    font-family: "Montserrat", sans-serif;
    font-weight: 700;
    font-size: 15.5px;
    line-height: 20px;
    letter-spacing: 1.6px;
    white-space: nowrap;
  }
  .services__sep { margin: 0 5px; }
</style>
</head>
<body>
<main class="canvas">
  <section class="card card--front" aria-label="Business card, light version">
    <p class="contact-line">Dean Marwick - 519 374 2083</p>
    <h1 class="wordmark">
      <span class="wordmark__name">BRIGHTWAY</span>
      <span class="wordmark__trade">AUTOMOTIVE &amp; DIESEL REPAIR</span>
    </h1>
    <div class="divider"></div>
    <p class="services">ROADSIDE ASSISTANCE<span class="services__sep">•</span>MOBILE REPAIRS<span class="services__sep">•</span>DIESEL REPAIRS<span class="services__sep">•</span>FLEET MAINTENANCE</p>
  </section>

  <section class="card card--back" aria-label="Business card, dark version">
    <p class="contact-line">Dean Marwick - 519 374 2083</p>
    <h2 class="wordmark">
      <span class="wordmark__name">BRIGHTWAY</span>
      <span class="wordmark__trade">AUTOMOTIVE &amp; DIESEL REPAIR</span>
    </h2>
    <div class="divider"></div>
    <p class="services">ROADSIDE ASSISTANCE<span class="services__sep">•</span>MOBILE REPAIRS<span class="services__sep">•</span>DIESEL REPAIRS<span class="services__sep">•</span>FLEET MAINTENANCE</p>
  </section>
</main>
</body>
</html>
```